Enhancement Of Draft Website - www.skylarkvolt.com

The website www.skylarkvolt.com exists but needs further development. With the exception of a small number of pages, the website is populated with the majority of content it requires. I would like a designer to review the design of the website and propose an enhanced design paying particular consideration to the following:

-Setting an appropriate colour scheme that matches with the company logo
-Ensuring the company logo is displayed appropriately on the website
-Making any other appropriate adjustments (through the selection of another theme / the customisation of the existing template) that improve the experience of the user on the website

An XML export file from the existing website is attached.

Target Market(s)

Specialist website targeting engineers working in aerospace companies

Industry/Entity Type

Engineer

Font styles to use
Sans Serif

Requirements
Must have
• Responsive design working across platforms. Contact form. Ease of use.

```html
<!DOCTYPE html>
<html lang="en">
<head>
<meta charset="utf-8">
<title>SkylarkVolt – High Voltage Training</title>
<link href="https://fonts.googleapis.com/css2?family=Open+Sans:wght@300;400;600;700;800&display=swap" rel="stylesheet">
<style>
  :root {
    --canvas: #eef3f7;
    --white: #ffffff;
    --ink: #2b2f36;
    --ink-soft: #3c424a;
    --link: #2f5f96;
    --brand: #2c4f7c;
    --footer: #182d54;
    --footer-text: #9fb0c8;
    --footer-accent: #5ba8e6;
    --tile-blue: #3a6b9e;
  }
  * { box-sizing: border-box; margin: 0; padding: 0; }
  html, body { width: 1200px; height: 1200px; overflow: hidden; }
  body { background: var(--canvas); font-family: "Open Sans", sans-serif; color: var(--ink); position: relative; }

  .page { position: absolute; left: 281px; top: 83px; width: 638px; height: 1047px; background: var(--white); overflow: hidden; }

  .site-header { position: absolute; top: 0; left: 0; width: 100%; height: 45px; display: flex; align-items: center; justify-content: space-between; padding: 0 22px 0 40px; }
  .brand { display: flex; align-items: center; gap: 6px; font-size: 20px; font-weight: 600; color: var(--brand); letter-spacing: -0.3px; }
  .brand-mark { width: 13px; height: 13px; background: var(--brand); }
  .main-nav { display: flex; gap: 14px; font-size: 10px; color: var(--ink-soft); }

  .hero { position: absolute; top: 45px; left: 0; width: 638px; height: 255px;
    background: radial-gradient(ellipse 60% 40% at 55% 100%, #c8dcef 0%, #5d86b3 35%, transparent 100%),
                linear-gradient(180deg, #1e3b63 0%, #2a5283 60%, #23456f 100%); }
  .hero-copy { position: absolute; top: 102px; left: 0; width: 100%; text-align: center; color: var(--white); }
  .hero-title { font-size: 18px; font-weight: 800; letter-spacing: 0.3px; line-height: 24px; }
  .hero-sub { margin-top: 2px; font-size: 12.5px; font-weight: 300; line-height: 19px; }

  .section-title { position: absolute; left: 0; width: 100%; text-align: center; font-size: 23px; font-weight: 300; line-height: 30px; color: var(--ink); }

  .feature { position: absolute; top: 384px; width: 160px; }
  .feature-head { display: flex; align-items: center; justify-content: center; gap: 7px; font-size: 14px; line-height: 20px; color: var(--ink); margin-bottom: 11px; }
  .feature-head svg { width: 15px; height: 15px; fill: var(--brand); }
  .feature p { font-size: 8.5px; line-height: 13.5px; color: var(--ink-soft); margin-bottom: 13px; }
  .feature a { display: block; font-size: 8.5px; line-height: 13.5px; color: var(--link); text-decoration: none; }
  .feature-rule { position: absolute; top: 503px; width: 180px; height: 4px; border-radius: 50%; box-shadow: 0 2px 3px rgba(0,0,0,0.18); }

  .basics-band { position: absolute; top: 540px; left: 0; width: 100%; height: 411px;
    background: linear-gradient(180deg, #ffffff 0%, #e5edf4 20%, #dfe8f1 55%, #eef3f8 85%, #ffffff 100%); }
  .tile { position: absolute; width: 166px; height: 124px; display: flex; flex-direction: column; align-items: center; justify-content: center; text-align: center; color: var(--white); font-size: 10px; font-weight: 700; line-height: 13.5px; text-shadow: 0 1px 2px rgba(0,0,0,0.5); }
  .tile svg { margin-top: 5px; width: 12px; height: 12px; fill: none; stroke: var(--white); stroke-width: 1.6; }
  .tile-pd-machines { background: var(--tile-blue); }
  .tile-discharge-type { background: linear-gradient(160deg, #3b4149 0%, #22272d 100%); }
  .tile-clearances { background: linear-gradient(120deg, #3a3531 0%, #5a524a 45%, #2a4f9c 75%, #2452a6 100%); }
  .tile-partial-a { background: linear-gradient(180deg, #8a8e93 0%, #b9bcc0 50%, #6f7378 100%); }
  .tile-partial-b { background: radial-gradient(ellipse at 60% 50%, #5b5fa8 0%, #2a2c5e 45%, #12142b 100%); }
  .tile-hv-testing { background: linear-gradient(135deg, #2e6fb3 0%, #c9948a 50%, #2b5a9a 100%); }

  .site-footer { position: absolute; top: 951px; left: 0; width: 638px; height: 96px; background: var(--footer); color: var(--footer-text); }
  .footer-brand { position: absolute; left: 41px; top: 17px; display: flex; align-items: center; gap: 6px; font-size: 16px; line-height: 20px; font-weight: 600; color: var(--footer-accent); }
  .footer-brand .brand-mark { width: 11px; height: 11px; background: var(--footer-accent); }
  .footer-legal { position: absolute; left: 41px; top: 50px; font-size: 8px; line-height: 13.5px; }
  .footer-contact { position: absolute; left: 420px; top: 14px; }
  .footer-contact h3 { font-size: 8.5px; line-height: 12px; font-weight: 400; margin-bottom: 9px; }
  .footer-contact p { display: flex; align-items: center; gap: 6px; font-size: 8px; line-height: 12px; }
  .footer-contact svg { width: 12px; height: 9px; fill: var(--footer-accent); }
</style>
</head>
<body>
<div class="page">
  <header class="site-header">
    <div class="brand"><span class="brand-mark"></span>SkylarkVolt</div>
    <nav class="main-nav">
      <span>Engineering</span><span>Testing</span><span>Training</span><span>HV Basics</span><span>About Us</span><span>Contact Us</span>
    </nav>
  </header>

  <section class="hero" role="img" aria-label="Passenger jet climbing through a blue evening sky">
    <div class="hero-copy">
      <h1 class="hero-title">HIGH VOLTAGE TRAINING</h1>
      <p class="hero-sub">Essential knowledge for those involved in the design, operation and<br>maintenance of HV systems in aerospace applications</p>
    </div>
  </section>

  <h2 class="section-title" style="top:322px">Our Features</h2>

  <div class="feature" style="left:32px">
    <div class="feature-head">
      <svg viewBox="0 0 16 16"><circle cx="6" cy="9" r="4"/><circle cx="6" cy="9" r="1.5" fill="#fff"/><circle cx="12" cy="4" r="3"/><circle cx="12" cy="4" r="1" fill="#fff"/></svg>
      Engineering
    </div>
    <p>Supporting the design of new HV systems and components for use in aerospace environments</p>
    <a href="#">Our range of engineering services and design tools &nbsp;»</a>
  </div>
  <div class="feature-rule" style="left:20px"></div>

  <div class="feature" style="left:239px">
    <div class="feature-head">
      <svg viewBox="0 0 16 16"><path d="M1 12a7 7 0 0 1 14 0z"/><path d="M8 11l3-5" stroke="#fff" stroke-width="1.5"/></svg>
      Testing
    </div>
    <p>Access to a full range of testing services to validate the performance of HV systems</p>
    <a href="#">Testing capabilities &nbsp;»</a>
  </div>
  <div class="feature-rule" style="left:232px"></div>

  <div class="feature" style="left:447px">
    <div class="feature-head">
      <svg viewBox="0 0 16 16" style="fill:none;stroke:#2c4f7c;stroke-width:1.4"><path d="M15 1L1 7l6 2 2 6z"/><path d="M15 1L7 9"/></svg>
      Training
    </div>
    <p>Online and face to face training provi-<br>sion to support your workforce</p>
    <a href="#">Details of our training options &nbsp;»</a>
  </div>
  <div class="feature-rule" style="left:440px"></div>

  <div class="basics-band"></div>
  <h2 class="section-title" style="top:560px">HV Basics</h2>
  <div class="tile tile-pd-machines" style="left:41px;top:609px" role="img" aria-label="Electrical machine stator laminations in blue">
    PD IN ELECTRICAL<br>MACHINES
    <svg viewBox="0 0 16 16"><path d="M15 1L1 7l6 2 2 6z"/><path d="M15 1L7 9"/></svg>
  </div>
  <div class="tile tile-discharge-type" style="left:231px;top:609px" role="img" aria-label="Electric arc between two electrodes">ELECTRICAL DISCHARGE<br>TYPE</div>
  <div class="tile tile-clearances" style="left:420px;top:609px" role="img" aria-label="Close-up of circuit board connectors">CLEARANCES</div>
  <div class="tile tile-partial-a" style="left:41px;top:759px" role="img" aria-label="Row of terminal block connectors with wires">PARTIAL DISCHARGE</div>
  <div class="tile tile-partial-b" style="left:231px;top:759px" role="img" aria-label="Lightning bolt on dark purple sky">PARTIAL DISCHARGE</div>
  <div class="tile tile-hv-testing" style="left:420px;top:759px" role="img" aria-label="Hand adjusting test equipment">HV TESTING</div>

  <footer class="site-footer">
    <div class="footer-brand"><span class="brand-mark"></span>SkylarkVolt</div>
    <p class="footer-legal">Voltline Design Ltd trading as SkylarkVolt -<br>Registered in England and Wales,<br>company number 0473921</p>
    <div class="footer-contact">
      <h3>CONTACT US</h3>
      <p><svg viewBox="0 0 12 9"><path d="M0 0h12v1.5L6 5 0 1.5z"/><path d="M0 3l6 3.5L12 3v6H0z"/></svg>: info@skylarkvolt.com</p>
    </div>
  </footer>
</div>
</body>
</html>
```